Black Friday Sale Social Media Graphics

Focusing on Black Friday Graphics for each of the pics attached.  So need the product pics turned into  social media graphics (square size). For the color scheme of the graphics, they should all be complementary to the product colors.
You can add any of the stock photography attached but none are required. I mainly need BOLD text that says:
Black Friday Sale
Up to $15 Off
If you wanted to add smaller text, these headlines can work:
1.	Burn Belly Fat Fast!
2.	Double Your Weight Loss With Our Supplements!
3.	Lose Weight Naturally: Ditch the Prescription Pills & Needles!
4.	Tired of Stubborn Belly Fat? Discover What Works!
5.	Melt Away Belly Fat Faster with Our Supplements!
6.	Struggling to Lose Weight? Discover the Ultimate Solution!
7.	Ready to Burn Fat Faster?

Target Market(s)
women trying to lose weight
Industry/Entity Type
health and wellness
Requirements
Must have
- the product pics attached

Nice to have
- Bold text that says: Black Friday Sale

```html
<!DOCTYPE html>
<html lang="en">
<head>
<meta charset="utf-8">
<title>Black Friday Sale Social Set</title>
<link href="https://fonts.googleapis.com/css2?family=Poppins:wght@400;600;800;900&family=Playball&family=Great+Vibes&display=swap" rel="stylesheet">
<style>
  :root{
    --ink:#0b0b0b;
    --teal-dark:#2c5a53;
    --green-1:#93d0bf;
    --green-2:#5b9e88;
    --green-3:#347765;
    --green-4:#3d5c52;
    --mint:#8ed9c4;
    --rose:#e6717f;
    --rose-soft:#f1b3d3;
    --rose-mid:#dc6fa6;
    --rose-deep:#a8548c;
    --sale-pink-a:#e88f9b;
    --sale-pink-b:#cc5d6c;
    --orchid:#df90b6;
    --violet-1:#433a80;
    --violet-2:#5a54a0;
    --violet-3:#7b77bf;
    --violet-4:#b3acec;
    --white:#ffffff;
    --grey-light:#dcdcdc;
  }
  *{box-sizing:border-box;margin:0;padding:0}
  html,body{width:1200px;height:1200px;overflow:hidden;background:var(--white)}
  .sheet{position:relative;width:1200px;height:1200px;border:2px solid var(--ink);border-radius:40px;background:var(--white)}
  .post{position:absolute;width:550px;height:550px;border:1px solid #444;border-radius:28px;overflow:hidden;font-family:'Poppins',sans-serif}
  .post--a{left:32px;top:32px;background:var(--white)}
  .post--b{left:616px;top:32px;background:var(--rose)}
  .post--c{left:32px;top:616px;background:var(--white)}
  .post--d{left:616px;top:616px;background:var(--orchid)}
  .post-bg{position:absolute;inset:0;width:550px;height:550px;z-index:0}
  .post-arrow{position:absolute;inset:0;width:550px;height:550px;z-index:3}
  .abs{position:absolute;z-index:2}
  .headline{font-weight:800;font-size:48px;letter-spacing:0.5px;line-height:1;white-space:nowrap}
  .sale-block{font-weight:900;font-size:98px;line-height:1;letter-spacing:1px}
  .product-shot{position:absolute;z-index:1;border-radius:18px;background:linear-gradient(160deg,#ffffff 0%,#eef0ef 55%,#d6dcd9 100%)}
  .tagline{font-size:12.5px;line-height:1.6;white-space:nowrap}
  .tagline b{font-weight:800}
  .script{font-family:'Great Vibes',cursive}
</style>
</head>
<body>
<div class="sheet">

  <!-- Post A -->
  <section class="post post--a">
    <svg class="post-bg" viewBox="0 0 550 550">
      <path d="M0,297 C120,272 250,335 360,378 C460,418 535,410 550,350 V550 H0 Z" fill="var(--rose-deep)"/>
      <path d="M0,300 C120,282 250,348 360,393 C460,432 535,438 550,390 V550 H0 Z" fill="var(--rose-mid)"/>
      <path d="M0,303 C120,292 250,360 360,410 C460,455 535,460 550,430 V550 H0 Z" fill="var(--rose-soft)"/>
    </svg>
    <div class="abs headline" style="left:93px;top:62px"><span style="color:var(--ink)">BLACK</span> <span style="color:var(--teal-dark)">FRIDAY</span></div>
    <div class="product-shot" role="img" aria-label="Four white supplement bottles with coloured labels, tilted in a row" style="left:145px;top:190px;width:330px;height:210px;transform:rotate(8deg)"></div>
    <div class="abs" style="left:170px;top:88px;font-family:'Playball',cursive;font-weight:400;font-size:108px;color:var(--ink);line-height:1;-webkit-text-stroke:2px var(--ink)">Sale</div>
    <div class="abs" style="left:60px;top:436px;display:flex;align-items:center;gap:14px;white-space:nowrap">
      <span style="font-size:46px;font-weight:400;color:var(--ink)">UP TO</span>
      <span style="font-size:98px;font-weight:900;color:var(--teal-dark);line-height:1">$15</span>
      <span style="font-size:46px;font-weight:400;color:var(--ink)">OFF</span>
    </div>
  </section>

  <!-- Post B -->
  <section class="post post--b">
    <svg class="post-bg" viewBox="0 0 550 550">
      <path d="M0,0 H110 C60,30 20,90 0,160 Z" fill="var(--green-1)"/>
      <path d="M0,0 H90 C45,35 15,95 0,150 Z" fill="var(--green-2)"/>
      <path d="M0,0 H70 C35,40 10,95 0,135 Z" fill="var(--green-3)"/>
      <path d="M0,430 C220,420 430,360 550,290 V550 H0 Z" fill="var(--green-4)"/>
      <path d="M0,480 C230,470 440,400 550,320 V550 H0 Z" fill="var(--green-3)"/>
      <path d="M110,550 C300,520 470,430 550,340 V550 Z" fill="var(--green-2)"/>
      <path d="M300,550 C420,500 510,430 550,380 V550 Z" fill="var(--green-1)"/>
    </svg>
    <svg class="post-arrow" viewBox="0 0 550 550">
      <path d="M288,356 C292,330 312,315 330,315 V303 L348,322 L330,341 V329 C312,329 298,340 288,356 Z" fill="none" stroke="var(--white)" stroke-width="4" stroke-linejoin="round"/>
    </svg>
    <div class="abs headline" style="left:103px;top:58px;color:var(--grey-light)">BLACK FRIDAY</div>
    <div class="abs sale-block" style="right:32px;top:96px;color:var(--mint)">SALE</div>
    <div class="product-shot" role="img" aria-label="Two cream pump bottles and a supplement jar" style="left:26px;top:115px;width:250px;height:305px"></div>
    <div class="abs" style="left:354px;top:227px;width:168px;height:244px;border:1px solid rgba(255,255,255,.7);border-radius:14px;background:rgba(255,255,255,.18);text-align:center">
      <div class="script" style="font-size:44px;color:var(--ink);margin-top:22px;line-height:1">Up to</div>
      <div style="font-size:62px;font-weight:800;color:var(--white);line-height:1.1;margin-top:10px">$15</div>
      <div style="font-size:46px;font-weight:400;color:var(--ink);line-height:1.1">OFF</div>
    </div>
    <div class="abs tagline" style="left:25px;top:452px;color:var(--white)">Melt Away <b>Belly Fat</b> Faster with Our Supplements!</div>
  </section>

  <!-- Post C -->
  <section class="post post--c">
    <svg class="post-bg" viewBox="0 0 550 550">
      <path d="M0,0 H420 C200,10 60,80 0,145 Z" fill="var(--green-1)"/>
      <path d="M0,0 H380 C180,20 50,90 0,140 Z" fill="var(--green-2)"/>
      <path d="M0,0 H330 C160,30 40,100 0,130 Z" fill="var(--green-3)"/>
      <path d="M0,435 C250,430 450,360 550,300 V550 H0 Z" fill="var(--green-4)"/>
      <path d="M0,470 C260,460 460,390 550,320 V550 H0 Z" fill="var(--green-3)"/>
      <path d="M0,545 C280,520 470,430 550,360 V550 H0 Z" fill="var(--green-2)"/>
      <path d="M250,550 C410,500 510,430 550,390 V550 Z" fill="var(--green-1)"/>
      <circle cx="443" cy="438" r="83" fill="var(--sale-pink-b)"/>
      <circle cx="443" cy="438" r="73" fill="none" stroke="#f3c2c8" stroke-width="1.2" stroke-dasharray="2 3"/>
    </svg>
    <svg class="post-arrow" viewBox="0 0 550 550">
      <path d="M336,492 C340,464 358,450 376,450 V440 L394,457 L376,474 V464 C360,464 347,474 336,492 Z" fill="none" stroke="var(--white)" stroke-width="4" stroke-linejoin="round"/>
    </svg>
    <div class="abs headline" style="left:109px;top:88px;color:var(--ink)">BLACK FRIDAY</div>
    <div class="product-shot" role="img" aria-label="Two cream pump bottles and a supplement jar" style="left:35px;top:150px;width:250px;height:375px"></div>
    <div class="abs sale-block" style="right:28px;top:130px;background:linear-gradient(90deg,var(--sale-pink-a),var(--sale-pink-b));-webkit-background-clip:text;background-clip:text;color:transparent">SALE</div>
    <div class="abs tagline" style="left:340px;top:256px;font-size:14px;color:var(--ink)">Melt Away <b>Belly Fat</b> Faster<br>with Our Supplements!</div>
    <div class="abs" style="left:395px;top:378px;width:100px;text-align:center">
      <div class="script" style="font-size:30px;color:#f6d8dc;line-height:1">Up to</div>
      <div style="font-size:44px;font-weight:800;color:var(--white);line-height:1.1">$15</div>
      <div style="font-size:28px;font-weight:400;color:var(--ink);line-height:1">OFF</div>
    </div>
  </section>

  <!-- Post D -->
  <section class="post post--d">
    <svg class="post-bg" viewBox="0 0 550 550">
      <path d="M550,20 C480,250 300,410 0,440 V550 H550 Z" fill="var(--violet-1)"/>
      <path d="M550,60 C500,290 380,450 150,550 H550 Z" fill="var(--violet-2)"/>
      <path d="M550,120 C520,330 430,470 300,550 H550 Z" fill="var(--violet-3)"/>
      <path d="M550,180 C540,360 490,480 420,550 H550 Z" fill="var(--violet-4)"/>
    </svg>
    <div class="abs headline" style="left:0;right:0;top:54px;text-align:center;color:var(--ink)">BLACK FRIDAY</div>
    <div class="abs sale-block" style="left:0;right:0;top:100px;text-align:center;color:var(--white)">SALE</div>
    <div class="abs" style="left:59px;top:214px;width:431px;height:60px;border:1px solid rgba(255,255,255,.6);border-radius:8px;background:rgba(110,70,150,.35);display:flex;align-items:center;justify-content:center;gap:14px;white-space:nowrap">
      <span style="font-size:38px;color:var(--ink)">Up to</span>
      <span style="font-size:44px;font-weight:800;color:var(--white)">$15</span>
      <span style="font-size:44px;font-weight:800;color:var(--mint)">OFF</span>
    </div>
    <div class="abs tagline" style="left:0;right:0;top:308px;text-align:center;font-size:16px;color:var(--white)">Melt Away <b>Belly Fat</b> Faster with Our Supplements!</div>
    <div class="product-shot" role="img" aria-label="Four white supplement bottles with coloured labels in a row" style="left:100px;top:355px;width:320px;height:190px"></div>
  </section>

</div>
</body>
</html>
```